Flyer Designer for a Widow and Door Company - loooking for fresh design

We are looking for a flyer designed to advertise our business - we supply and install windows and doors - we are looking for a fresh looking flyer to distribute to drum up business - more information can be found at our website www.brightpanehouse.co.uk - We want a different approach than we currently have - making it vibrant and fresh - you can see the services on the website but its more the graphical design that we are looking for rather than content as the content from the website can be used for each service etc.

Target Market(s)

the general public

Colors

Designer to choose colors to be used in the design.

Requirements
Must have
• vibrant design and images

```html
<!DOCTYPE html>
<html lang="en">
<head>
<meta charset="utf-8">
<title>Bright Pane House – Bespoke Windows and Doors Flyer</title>
<link href="https://fonts.googleapis.com/css2?family=Roboto+Condensed:ital,wght@0,400;0,700;1,700&family=Open+Sans:wght@400;600&display=swap" rel="stylesheet">
<style>
  :root {
    --brand-blue: #2a6cb8;
    --brand-blue-dark: #1f5596;
    --ink: #1f2328;
    --ink-soft: #3a3f46;
    --paper: #f7f5ef;
    --room-light: #fbf8ee;
    --room-mid: #e7e2d2;
    --room-warm: #d9cfb5;
    --footer-grey: #5b5f66;
    --footer-grey-dark: #44484e;
    --backdrop: #d8d8d8;
    --white: #ffffff;
  }
  * { box-sizing: border-box; margin: 0; padding: 0; }
  html, body { width: 1200px; height: 1000px; overflow: hidden; }
  body { background: var(--backdrop); position: relative; font-family: "Open Sans", Arial, sans-serif; color: var(--ink); }

  .flyer {
    position: absolute; left: 260px; top: 20px; width: 680px; height: 960px;
    background: var(--paper); overflow: hidden;
    box-shadow: 0 6px 24px rgba(0,0,0,.25);
  }
  .flyer__backdrop {
    position: absolute; inset: 0;
    background:
      linear-gradient(180deg, rgba(255,255,255,0) 0%, rgba(255,255,255,0) 70%, rgba(120,120,120,.25) 100%),
      radial-gradient(ellipse at 60% 40%, var(--room-light) 0%, var(--room-mid) 60%, var(--room-warm) 100%);
  }

  .headline {
    position: absolute; left: 34px; top: 58px; width: 380px;
    font-family: "Roboto Condensed", Arial, sans-serif; font-weight: 700;
    font-size: 30px; line-height: 1.15; color: var(--brand-blue);
  }
  .intro {
    position: absolute; left: 30px; top: 138px; width: 400px;
    font-size: 9.6px; line-height: 1.45; color: var(--ink-soft);
  }

  .hero-door { position: absolute; left: 452px; top: 40px; width: 196px; height: 184px; }

  .quote-banner {
    position: absolute; left: 370px; top: 294px; width: 294px; height: 44px;
    background: var(--brand-blue); color: var(--white);
    font-family: "Roboto Condensed", Arial, sans-serif; font-weight: 700; font-style: italic;
    font-size: 26px; line-height: 44px; text-align: center;
    box-shadow: 0 3px 6px rgba(0,0,0,.3);
  }

  .gallery { position: absolute; left: 50px; top: 300px; width: 280px; height: 560px; }

  .services { position: absolute; left: 364px; top: 350px; width: 300px; }
  .service { margin-bottom: 14px; }
  .service__title {
    font-family: "Roboto Condensed", Arial, sans-serif; font-weight: 700; font-size: 15px;
    color: var(--ink); text-transform: uppercase;
  }
  .service__title span { color: var(--brand-blue); }
  .service__lead { font-size: 9.2px; line-height: 1.35; color: var(--ink-soft); margin: 2px 0 6px; }
  .service__list {
    list-style: none; display: grid; grid-template-columns: 1fr 1fr 1fr; gap: 4px 8px;
    font-family: "Roboto Condensed", Arial, sans-serif; font-weight: 700; font-size: 11.5px;
    color: var(--brand-blue);
  }
  .service__list li { position: relative; padding-left: 10px; line-height: 1.05; }
  .service__list li::before {
    content: ""; position: absolute; left: 0; top: 3px; width: 5px; height: 5px; background: var(--brand-blue);
  }

  .brand-mark {
    position: absolute; left: 372px; top: 820px; display: flex; align-items: center; gap: 10px;
    white-space: nowrap;
  }
  .brand-mark__square { width: 34px; height: 34px; background: var(--brand-blue); flex: none; }
  .brand-mark__name {
    font-family: "Roboto Condensed", Arial, sans-serif; font-weight: 700; font-size: 30px;
    color: var(--brand-blue); letter-spacing: .5px; line-height: 1;
  }

  .footer { position: absolute; left: 0; bottom: 0; width: 680px; height: 68px; }
  .footer__address {
    position: absolute; left: 0; top: 0; width: 340px; height: 68px;
    background: var(--brand-blue);
    clip-path: polygon(0 0, 88% 0, 100% 100%, 0 100%);
    color: var(--white); font-size: 10px; font-weight: 600; line-height: 1.4;
    padding: 20px 0 0 28px; white-space: nowrap;
  }
  .footer__contact {
    position: absolute; right: 0; top: 0; width: 380px; height: 68px;
    background: linear-gradient(180deg, var(--footer-grey), var(--footer-grey-dark));
    clip-path: polygon(10% 0, 100% 0, 100% 100%, 0 100%);
    color: var(--white); font-size: 9.5px; line-height: 1.7;
    padding: 18px 12px 0 66px;
    display: flex; gap: 16px; white-space: nowrap;
  }
  .footer__contact b { font-weight: 600; display: inline-block; width: 38px; }
  .footer__contact .icon { display: inline-block; width: 8px; height: 8px; vertical-align: -1px; margin-right: 4px; }
</style>
</head>
<body>
  <article class="flyer">
    <div class="flyer__backdrop" role="img" aria-label="Soft-focus photograph of a bright conservatory interior with chequered floor"></div>

    <h1 class="headline">Installers and Suppliers of Bespoke Windows and Doors</h1>
    <p class="intro">The Bright Pane House team have many years’ experience supplying and fitting the highest quality windows and doors throughout Northamptonshire. Our experienced, friendly team are able to offer a personal touch to your project ensuring you are fully informed at all times and completely happy with the product choices you have made. All of our surveying is kept in house by our installation team which has been selected to carry out your installation. This ensures that when our team arrive at your home to install your windows and doors, you can be confident that your installation will be a smooth process with no surprises</p>

    <svg class="hero-door" viewBox="0 0 196 184" role="img" aria-label="Photograph of a black front door set in a stone wall">
      <polygon points="49,2 147,2 194,92 147,182 49,182 2,92" fill="#8f8470" stroke="#ffffff" stroke-width="3"/>
    </svg>

    <div class="quote-banner">REQUEST A FREE QUOTE</div>

    <svg class="gallery" viewBox="0 0 280 560">
      <g stroke="#ffffff" stroke-width="3">
        <polygon role="img" aria-label="Photograph of white French doors" points="170,0 240,0 278,65 240,130 170,130 132,65" fill="#6f6a5c"/>
        <polygon role="img" aria-label="Photograph of white patio doors in brick" points="40,70 110,70 148,135 110,200 40,200 2,135" fill="#a8a196"/>
        <polygon role="img" aria-label="Photograph of a red composite front door" points="170,140 240,140 278,205 240,270 170,270 132,205" fill="#8d1f22"/>
        <polygon role="img" aria-label="Photograph of a grey glazed door" points="40,210 110,210 148,275 110,340 40,340 2,275" fill="#8fa3b3"/>
        <polygon role="img" aria-label="Photograph of a window inside a room" points="170,280 240,280 278,345 240,410 170,410 132,345" fill="#b7a486"/>
        <polygon role="img" aria-label="Photograph of a glazed door onto a garden" points="40,350 110,350 148,415 110,480 40,480 2,415" fill="#c9c3b4"/>
      </g>
    </svg>

    <section class="services">
      <div class="service">
        <h2 class="service__title">Our <span>Windows</span></h2>
        <p class="service__lead">At Bright Pane House we can supply and fit a huge range of window designs to suit your individual needs.</p>
        <ul class="service__list">
          <li>Casement</li><li>Tilt-and-Turn</li><li>Vertical slider / sash windows</li>
          <li>Bow or bay window</li><li>French windows</li>
        </ul>
      </div>
      <div class="service">
        <h2 class="service__title">Our <span>Doors</span></h2>
        <p class="service__lead">At Bright Pane House we can supply and fit a huge range of window designs to suit your individual needs.</p>
        <ul class="service__list">
          <li>Composite Doors</li><li>Bifolding Doors</li><li>uPVC Doors</li>
          <li>Patio Doors</li><li>French Doors</li><li>Stable Doors</li>
        </ul>
      </div>
      <div class="service">
        <h2 class="service__title">Repairs</h2>
        <ul class="service__list">
          <li>Window Repairs</li><li>Door Repairs</li><li>Glass Units</li>
          <li>Hardware</li><li>Adjustments</li><li>Cat Flap Services</li>
        </ul>
      </div>
      <div class="service">
        <h2 class="service__title">Landlord <span>Services</span></h2>
        <ul class="service__list">
          <li>Repairs</li><li>Replacments</li><li>Adjustments</li>
          <li>Surveys</li>
        </ul>
      </div>
    </section>

    <div class="brand-mark">
      <span class="brand-mark__square"></span>
      <span class="brand-mark__name">BRIGHT PANE HOUSE</span>
    </div>

    <footer class="footer">
      <div class="footer__address">Bright Pane House Riverside Court Mill Lane<br>Kettleford Northamptonshire NN9 4ZX</div>
      <div class="footer__contact">
        <div><b>Sales:</b><svg class="icon" viewBox="0 0 10 10"><path d="M2 1h2l1 2-1 1a6 6 0 0 0 2 2l1-1 2 1v2a1 1 0 0 1-1 1A8 8 0 0 1 1 2a1 1 0 0 1 1-1z" fill="#fff"/></svg>01632 960 260<br><b>Office:</b><svg class="icon" viewBox="0 0 10 10"><path d="M2 1h2l1 2-1 1a6 6 0 0 0 2 2l1-1 2 1v2a1 1 0 0 1-1 1A8 8 0 0 1 1 2a1 1 0 0 1 1-1z" fill="#fff"/></svg>01632 960 261</div>
        <div><svg class="icon" viewBox="0 0 10 10"><rect x="1" y="2" width="8" height="6" fill="none" stroke="#fff"/><path d="M1 2l4 3 4-3" fill="none" stroke="#fff"/></svg>sales@brightpanehouse.co.uk<br><svg class="icon" viewBox="0 0 10 10"><rect x="1" y="2" width="8" height="6" fill="none" stroke="#fff"/><path d="M1 2l4 3 4-3" fill="none" stroke="#fff"/></svg>enquires@brightpanehouse.co.uk</div>
      </div>
    </footer>
  </article>
</body>
</html>
```